Large online photo magazine needs redesign

We have previously digitised a historical photographic magazine of around 20,000 printed pages and made it available online. The magazine ran up to the early 1970s, and the content is largely black and white photographs of local events, accompanied by short captions.

Although the content is very rich, the design needs to be revisited so that:
* it is visually appealing
* it is responsive (i.e. works in browsers across all manner of devices)
* is faithful to the nature of the content

There are only a few core page types, and the central one is the article page, an example of which can be seen at:
http://lanternweekly.org.nz/gisborne/issue/KLW81_19600714/t1-body-d4.html

Any design submitted should be based on the treatment of an article page such as the above.

Given the large number of pages on our site, we need a design which can be templated to work for any content in the collection, i.e. we cannot hand-craft our templates to match a given page of content, rather a template must work acceptably well for all content.

The current site, although basic in design, has the advantage that it is quite efficient in the amount of data per page request (around 100k - 200k). While not adverse to web fonts, banner imagery etc, we will carefully consider the benefit gained from any such treatment against the amount of extra data that needs to be downloaded to the client's browser.

For the right design, we are able ourselves to adapt it to a CSS layout.

An example of each core page type is as follows (though for this project we only expect a design for a single page, as itemised above):

http://lanternweekly.org.nz/gisborne/index.html
http://lanternweekly.org.nz/gisborne/about.html
http://lanternweekly.org.nz/gisborne/help.html
http://lanternweekly.org.nz/gisborne/initial/index.html
http://lanternweekly.org.nz/gisborne/search/results?type=section&text=smith&cmdSubmit=Go
http://lanternweekly.org.nz/gisborne/advanced-search/index.html
http://lanternweekly.org.nz/gisborne/issue/KLW81_19600714/t1-front-d1.html
http://lanternweekly.org.nz/gisborne/issue/KLW81_19600714/index.html
http://lanternweekly.org.nz/gisborne/issue/KLW81_19600714/fig-KLW81_19600714_005a.html
http://lanternweekly.org.nz/gisborne/issue/KLW81_19600714/KLW81_19600714_012.html
http://lanternweekly.org.nz/gisborne/issue/KLW81_19600714/thumbnails.html

Target Market(s)

A general browsing audience of all ages, but skewed towards the older generations, and those interested in family / regional history.

The average user will not be particularly web-savy, and the treatment of the content should not detract / distract from the actual content itself.

Industry/Entity Type

Events

Requirements
Must have
• * it is visually appealing
The content should be visually appealing to the audience, which can be defined as a general browsing audience of all ages, but skewed towards the middle and older generations.

* it is responsive (the design can be adapted - by us - to work in browsers across all manner of devices)

The magazine covers (http://lanternweekly.org.nz/gisborne/issues/index.html) offer some possible inspiration for treatment of the material.

```html
<!DOCTYPE html>
<html lang="en">
<head>
<meta charset="utf-8">
<title>Lantern Weekly – Flying Sisters from Gisborne</title>
<link rel="stylesheet" href="https://fonts.googleapis.com/css2?family=Oxygen:wght@300;400;700&display=swap">
<style>
:root{
  --brand:#c93a4e;
  --brand-btn:#cf3b52;
  --nav:#3e0c1c;
  --dark-btn:#2c0611;
  --page:#f2f2f2;
  --panel:#ffffff;
  --bar:#f7f4e9;
  --bar-line:#e6e0cc;
  --text:#7a7a7a;
  --heading:#555;
  --rule:#dddddd;
}
*{box-sizing:border-box;margin:0;padding:0}
html,body{width:1199px;height:1200px;overflow:hidden}
body{background:var(--page);font-family:"Oxygen",sans-serif;position:relative;color:var(--text)}
a{text-decoration:none;color:inherit}
.site-header{position:absolute;left:0;top:0;width:1199px;height:104px;background:var(--brand)}
.brand{position:absolute;left:98px;top:28px;color:#fff;font-size:40px;font-weight:700;letter-spacing:1px}
.search{position:absolute;left:884px;top:59px;width:225px;height:29px;border:1px solid #e58a97;background:#bf3347;display:flex;align-items:center;padding-left:10px;font-size:11px;font-style:italic;color:#f4d2d7}
.search svg{position:absolute;right:9px;top:6px}
.main-nav{position:absolute;left:0;top:104px;width:1199px;height:46px;background:var(--nav);display:flex;padding-left:95px}
.main-nav a{color:#fff;font-size:13.5px;font-weight:700;display:flex;align-items:center;padding:0 19px 0 17px;border-right:1px solid #6a3041;height:46px}
.panel{position:absolute;left:87px;top:150px;width:1024px;height:980px;background:var(--panel)}
.issue-bar{position:absolute;left:108px;top:190px;width:986px;height:60px;background:var(--bar);border:1px solid var(--bar-line);border-radius:2px}
.btn{position:absolute;height:31px;border-radius:16px;color:#fff;font-size:14px;display:flex;align-items:center;justify-content:center;box-shadow:0 0 0 1px #fff inset}
.btn-dark{background:var(--dark-btn)}
.btn-red{background:var(--brand-btn)}
.issue-title{position:absolute;left:22px;right:0;top:12px;text-align:center;color:var(--brand);font-size:28px;font-weight:300}
.page-thumb{position:absolute;left:470px;top:277px;width:270px;height:176px;border:1px solid #ddd;background:#fff;padding:5px;box-shadow:0 1px 3px rgba(0,0,0,.15)}
.fill{width:100%;height:100%}
.fill-photo{background:linear-gradient(135deg,#6e6a61,#b8b2a2 55%,#d9d3c3)}
.fill-page{background:linear-gradient(135deg,#5d5a53,#c4bca8 50%,#8a8478)}
.arrow{position:absolute;top:320px}
.rule{position:absolute;left:108px;top:487px;width:984px;height:1px;background:var(--rule)}
.article-title{position:absolute;left:12px;width:1199px;top:509px;text-align:center;color:var(--brand);font-size:21px;font-weight:400}
.card{position:absolute;top:555px;width:290px;height:468px;border:1px solid #cfcfcf;border-radius:4px;background:linear-gradient(#fff 60%,#f1f1f1)}
.card .frame{position:absolute;left:29px;top:21px;width:232px;background:#fff;border:1px solid #ddd;padding:5px;box-shadow:0 1px 3px rgba(0,0,0,.12)}
.card h3{position:absolute;left:0;right:0;top:175px;text-align:center;font-weight:400;color:var(--heading);font-size:17.5px}
.card p{position:absolute;left:10px;right:10px;text-align:center;font-size:13px;line-height:22px;font-weight:300;color:#777}
.site-footer{position:absolute;left:14px;width:1199px;top:1155px;text-align:center;font-size:13px;color:#555;font-weight:300}
</style>
</head>
<body>
<header class="site-header">
  <a class="brand" href="http://lanternweekly.org.nz/gisborne/index.html">Lantern Weekly</a>
  <div class="search">Search photos news
    <svg width="16" height="16" viewBox="0 0 16 16"><circle cx="6.5" cy="6.5" r="5" fill="none" stroke="#fff" stroke-width="2"/><line x1="10" y1="10" x2="14.5" y2="14.5" stroke="#fff" stroke-width="2"/></svg>
  </div>
</header>
<nav class="main-nav">
  <a href="http://lanternweekly.org.nz/gisborne/index.html">HOME</a>
  <a href="http://lanternweekly.org.nz/gisborne/about.html">ABOUT</a>
  <a href="http://lanternweekly.org.nz/gisborne/issues/index.html">BROWSE LANTERN WEEKLY</a>
  <a href="http://lanternweekly.org.nz/gisborne/initial/index.html">A-Z PEOPLE</a>
  <a href="http://lanternweekly.org.nz/gisborne/help.html">HELP</a>
</nav>
<main class="panel"></main>

<div class="issue-bar">
  <a class="btn btn-dark" style="left:22px;top:14px;width:121px" href="#">Previous article</a>
  <a class="btn btn-red" style="left:152px;top:14px;width:114px" href="http://lanternweekly.org.nz/gisborne/issue/KLW81_19600714/index.html">Issue content</a>
  <div class="issue-title">No 73 July 14, 1960</div>
  <a class="btn btn-red" style="left:740px;top:14px;width:114px" href="#">Print article</a>
  <a class="btn btn-dark" style="left:860px;top:14px;width:114px" href="#">Next article</a>
</div>

<svg class="arrow" style="left:376px" width="40" height="86" viewBox="0 0 40 86"><polyline points="38,1 3,43 38,85" fill="none" stroke="#777" stroke-width="1.3"/></svg>
<div class="page-thumb"><div class="fill fill-page" role="img" aria-label="Magazine page spread with portrait photographs and a river bridge picture"></div></div>
<svg class="arrow" style="left:807px" width="40" height="86" viewBox="0 0 40 86"><polyline points="2,1 37,43 2,85" fill="none" stroke="#777" stroke-width="1.3"/></svg>

<div class="rule"></div>
<h1 class="article-title">Flying Sisters from Gisborne</h1>

<article class="card" style="left:144px">
  <div class="frame" style="height:260px"><div class="fill fill-photo" role="img" aria-label="Photograph of three sisters in air hostess uniforms with printed caption"></div></div>
  <p style="top:291px">This is probably something of a record--three sisters who are all air hostesses. They are the Harlow sisters.....Celeste, Ivy, and Lorraine, daughters of Mr and Mrs W. G. Harlow, Kowhai Road, Gisborne.</p>
</article>

<article class="card" style="left:457px">
  <div class="frame" style="height:260px"><div class="fill fill-photo" role="img" aria-label="Photograph of an air hostess standing in an aircraft doorway"></div></div>
  <p style="top:291px">And this young lady, Margery Lindqvist, of Auckland, has made history in another way. She was the first air hostess to make a scheduled flight to Gisborne, on Sunday of last week. Hostess service has been extended by C.A.S. to include Gisborne flights, beginning with the Sunday Services.</p>
</article>

<article class="card" style="left:770px">
  <div class="frame" style="height:141px"><div class="fill fill-photo" role="img" aria-label="Photograph of an old truss bridge over a river with printed caption"></div></div>
  <h3>Bridge In Splints</h3>
  <p style="top:203px;left:24px;right:24px">The old highway bridge across the Waiapu River near Ruatoria probably has more Bailey "splints" than any other bridge in the country. It is to be replaced soon by a modern structure two miles downstream, after which all main-route traffic will pass through Ruatoria township. (Picture, Eastcape Studio).</p>
</article>

<a class="btn btn-dark" style="left:391px;top:1057px;width:121px" href="#">Previous article</a>
<a class="btn btn-red" style="left:526px;top:1054px;width:115px" href="http://lanternweekly.org.nz/gisborne/issue/KLW81_19600714/index.html">Issue content</a>
<a class="btn btn-dark" style="left:657px;top:1053px;width:114px" href="#">Next article</a>

<footer class="site-footer">© 2012 Harbourside Memorial Library</footer>
</body>
</html>
```